Personal training company in the fitness industry

Training

(Front of card)
Forge Hour Fitness
417 Calloway Street Canningvale 6155 (Inside VelaGym36 complex)
Tomas Halvorsk
Personal Trainer
halvtomas@brentlo.net
0417 203 958
Back of card
One on One Training
Group Training (min 3)
Outdoor bootcamps
Workout programs
Meal guides
Competition preparation
(bottom middle of card)
GET THAT FORGE ON!

```html
<!DOCTYPE html>
<html lang="en">
<head>
<meta charset="utf-8">
<title>Forge Hour Fitness – Business Card</title>
<link rel="stylesheet" href="https://fonts.googleapis.com/css2?family=Open+Sans:wght@400;600;700&display=swap">
<style>
  :root {
    --amber: #f8a51d;
    --ink: #050505;
    --paper: #ffffff;
    --silver: #d2d2d2;
    --backdrop: #8d8d8d;
  }
  * { margin: 0; padding: 0; box-sizing: border-box; }
  html, body { width: 1200px; height: 900px; overflow: hidden; }
  body {
    background: var(--backdrop);
    font-family: "Open Sans", Arial, sans-serif;
    color: var(--paper);
    position: relative;
  }

  .card {
    position: absolute;
    overflow: hidden;
    box-shadow: 0 10px 24px rgba(0,0,0,.35);
  }

  /* ---------- back of card ---------- */
  .card--back {
    left: 560px; top: 80px;
    width: 560px; height: 320px;
    background: var(--amber);
  }
  .card--back .black-field {
    position: absolute; left: 0; right: 0; top: 52px; height: 222px;
    background: var(--ink);
  }
  .services {
    position: absolute; top: 7px; left: 20px; right: 20px;
    text-align: right;
    font-size: 11.5px; line-height: 19px; font-weight: 400; letter-spacing: .2px;
  }
  .services span { margin: 0 5px; }
  .back-brand {
    position: absolute; left: 0; right: 0; top: 100px;
    display: flex; align-items: center; justify-content: center; gap: 14px;
  }
  .brand-dot {
    width: 34px; height: 34px; border-radius: 50%;
    background: var(--amber);
    flex: none;
  }
  .brand-name {
    font-weight: 700; color: var(--amber);
    font-size: 34px; letter-spacing: .5px; line-height: 1;
    white-space: nowrap;
  }
  .slogan {
    position: absolute; left: 0; right: 0; top: 238px;
    text-align: center; font-weight: 700; font-size: 13px; letter-spacing: .3px;
  }

  /* ---------- front of card ---------- */
  .card--front {
    left: 70px; top: 440px;
    width: 640px; height: 366px;
    background: var(--amber);
  }
  .card--front .black-field {
    position: absolute; left: 0; right: 0; top: 0; height: 150px;
    background: var(--ink);
  }
  .card--front .base-strip {
    position: absolute; left: 0; right: 0; bottom: 0; height: 24px;
    background: var(--ink);
  }
  .front-brand {
    position: absolute; right: 34px; top: 52px;
    display: flex; align-items: center; gap: 14px;
  }
  .front-brand .brand-name { font-size: 38px; }
  .front-brand .brand-dot { width: 38px; height: 38px; background: var(--silver); }

  .person { position: absolute; left: 30px; top: 166px; }
  .person__name { font-weight: 700; font-size: 22px; line-height: 1.15; }
  .person__role { font-weight: 400; font-size: 14px; }

  .contacts {
    position: absolute; right: 30px; left: 30px; top: 252px;
    list-style: none; text-align: right;
    font-size: 16px; line-height: 24px;
  }
  .contacts li { display: flex; justify-content: flex-end; align-items: center; gap: 10px; white-space: nowrap; }
  .contacts svg { width: 13px; height: 13px; fill: var(--paper); flex: none; }
</style>
</head>
<body>

  <section class="card card--back" aria-label="Back of business card">
    <div class="black-field"></div>
    <p class="services">One on One Training<span>|</span>Group Training (min 3)<span>|</span>Outdoor bootcamps<br>Workout programs<span>|</span>Meal guides<span>|</span>Competition preparation</p>
    <div class="back-brand">
      <div class="brand-dot"></div>
      <div class="brand-name">Forge Hour Fitness</div>
    </div>
    <p class="slogan">GET THAT FORGE ON!</p>
  </section>

  <section class="card card--front" aria-label="Front of business card">
    <div class="black-field"></div>
    <div class="base-strip"></div>

    <div class="front-brand">
      <div class="brand-dot"></div>
      <div class="brand-name">Forge Hour Fitness</div>
    </div>

    <div class="person">
      <p class="person__name">Tomas Halvorsk</p>
      <p class="person__role">Personal Trainer</p>
    </div>

    <ul class="contacts">
      <li>0417 203 958
        <svg viewBox="0 0 16 16" aria-hidden="true"><path d="M4 1h8v14H4zM5.5 3v8h5V3zM7 12.5h2v1H7z" fill-rule="evenodd"/></svg></li>
      <li>halvtomas@brentlo.net
        <svg viewBox="0 0 16 16" aria-hidden="true"><path d="M1 3h14v10H1zM2 4l6 5 6-5z" fill-rule="evenodd"/></svg></li>
      <li>417 Calloway Street Canningvale 6155 (Inside VelaGym36 complex)
        <svg viewBox="0 0 16 16" aria-hidden="true"><path d="M8 1a5 5 0 0 1 5 5c0 4-5 9-5 9S3 10 3 6a5 5 0 0 1 5-5zm0 3a2 2 0 1 0 0 4 2 2 0 0 0 0-4z" fill-rule="evenodd"/></svg></li>
    </ul>
  </section>

</body>
</html>
```